Designing business cards for my start-up business

The company is called Velloran. We are a start-up tech data company based in Guernsey, Channel Islands. We want the business cards to look clean, fresh and innovative, just what a tech company should be. We do not want the business cards to look corporate or too official such as a bank. I would like the front of the business card to have our logo and the tag line of "Linking Potential". On the back will be our contact details, emails etc. However I am open to your ideas and suggestions. I have provided all our logos and a word doc of all our contact details. There are 4 directors of the business, so I want 4 versions of the same design.

Target Market(s)

Our clients are businesses of all industries. Its a broad target market.

Industry/Entity Type

Information Technology

Contact Information for Business Card

I have attached a word doc called "Business Cards info" which gives all contact details of the 4 employees for the company.

Requirements
Must have
• We must have our logo and the tag line of "Linking Potential". This could on the front of the card and then the individuals contact details on the back. Other than that, I'm happy for the designers to come up with ideas/styles.
Nice to have
• N/A
Should not have
• I don't want the cards to look too formal or corporate. As mentioned, we are a tech start-up so we want to look innovative.

```html
<!DOCTYPE html>
<html lang="en">
<head>
<meta charset="utf-8">
<title>Velloran Business Card</title>
<link rel="stylesheet" href="https://fonts.googleapis.com/css2?family=Open+Sans:wght@400;600;700&display=swap">
<style>
  :root {
    --page-bg: #e9e9e9;
    --card-white: #ffffff;
    --card-grey: #dcdcdc;
    --accent: #e2462c;
    --accent-light: #ee6a4a;
    --ink: #6b6b6b;
    --ink-dark: #1e1e1e;
    --divider: #9a9a9a;
  }
  * { box-sizing: border-box; margin: 0; padding: 0; }
  html, body {
    width: 1200px; height: 900px; overflow: hidden;
    background: var(--page-bg);
    font-family: "Open Sans", sans-serif;
  }
  .canvas { position: relative; width: 1200px; height: 900px; }

  .card {
    position: absolute; left: 290px; width: 620px; height: 354px;
    background: var(--card-white);
    box-shadow: 0 6px 18px rgba(0,0,0,0.18);
    overflow: hidden;
  }
  .card--contact { top: 60px; background: linear-gradient(100deg, var(--card-grey) 0%, #f4f4f4 45%, var(--card-white) 70%); }
  .card--front { top: 484px; background: linear-gradient(120deg, var(--card-white) 40%, #ececec 100%); }

  .brand { position: absolute; display: flex; flex-direction: column; align-items: center; }
  .brand__mark { background: var(--accent); }
  .brand__name {
    font-weight: 700; color: var(--ink-dark);
    letter-spacing: 0.42em; padding-left: 0.42em;
  }
  .card--contact .brand { left: 62px; top: 56px; }
  .card--contact .brand__mark { width: 104px; height: 104px; }
  .card--contact .brand__name { font-size: 17px; margin-top: 12px; }
  .card--front .brand { left: 240px; top: 72px; }
  .card--front .brand__mark { width: 112px; height: 112px; }
  .card--front .brand__name { font-size: 18px; margin-top: 12px; }

  .divider {
    position: absolute; left: 262px; top: 44px; width: 1px; height: 146px;
    background: var(--divider);
  }
  .person { position: absolute; left: 340px; top: 70px; }
  .person__name { font-size: 24px; font-weight: 700; color: var(--ink); letter-spacing: -0.01em; }
  .person__role { font-size: 14px; color: var(--ink); margin-left: 20px; margin-top: 2px; }

  .contact-band {
    position: absolute; left: 0; top: 212px; width: 100%; height: 96px;
    background: linear-gradient(90deg, var(--accent) 0%, var(--accent-light) 40%, var(--accent) 100%);
    border-top: 2px solid #f6d6cf;
    padding: 24px 0 0 100px;
    color: #fff; font-size: 13px; line-height: 24px;
  }
  .contact-line { display: flex; align-items: center; gap: 5px; white-space: nowrap; }
  .contact-line svg { width: 11px; height: 11px; fill: var(--ink-dark); flex: none; }
  .contact-sep { display: inline-block; width: 1px; height: 14px; background: rgba(255,255,255,0.7); margin: 0 6px; }

  .frame { position: absolute; inset: 0; }
  .tagline {
    position: absolute; left: 258px; top: 290px;
    font-size: 19px; color: #3a3a3a; letter-spacing: -0.01em;
  }
</style>
</head>
<body>
<main class="canvas">

  <section class="card card--contact" aria-label="Business card, contact side">
    <div class="brand">
      <div class="brand__mark"></div>
      <div class="brand__name">Velloran</div>
    </div>
    <div class="divider"></div>
    <div class="person">
      <div class="person__name">ELISE MARTEL</div>
      <div class="person__role">Director</div>
    </div>
    <div class="contact-band">
      <div class="contact-line">
        <svg viewBox="0 0 12 12"><path d="M6 1 L11 6 H9.5 V11 H7 V8 H5 V11 H2.5 V6 H1 Z"/></svg>
        <span>: 14 Rue des Vaux, Port Marlow, Isle of Carrow, KM4 2QX, Northern Isles,</span>
      </div>
      <div class="contact-line">
        <svg viewBox="0 0 12 12"><path d="M2.5 1 L4.5 1 L5.3 3.6 L4 4.6 Q5 7 7.4 8 L8.4 6.7 L11 7.5 L11 9.5 Q10 11 8.5 11 Q2 9.5 1 3.5 Q1 2 2.5 1 Z"/></svg>
        <span>: +44 7700 900 318,</span><span class="contact-sep"></span>
        <svg viewBox="0 0 12 12"><path d="M1 2.5 H11 V9.5 H1 Z M1.8 3.2 L6 6.4 L10.2 3.2 V8.8 H1.8 Z" fill-rule="evenodd"/></svg>
        <span>: Elise.Martel@velloran.io,</span><span class="contact-sep"></span>
        <svg viewBox="0 0 12 12"><circle cx="6" cy="6" r="5"/></svg>
        <span>: www.velloran.io</span>
      </div>
    </div>
  </section>

  <section class="card card--front" aria-label="Business card, front side">
    <svg class="frame" viewBox="0 0 620 354" width="620" height="354" aria-hidden="true">
      <path d="M40 30 H580 V262 H440 V282 H250 V318 H40 Z" fill="none" stroke="var(--accent)" stroke-width="1.6"/>
    </svg>
    <div class="brand">
      <div class="brand__mark"></div>
      <div class="brand__name">Velloran</div>
    </div>
    <div class="tagline">LINKING POTENTIAL</div>
  </section>

</main>
</body>
</html>
```